Senior Benefits checkup postcard

develop oversize postcard for direct mail campaign for senior market insurance agency. Targeting seniors ages 50-80. offering a no cost or free benefits checkup for Life, Health and wealth protection.. Posing questions to seniors Such as. *With over 280 insurance companies in our state, How do you find the right plan?* Can I save money on my bravonel plan? Who covers my illnesses? Is my life insurance policy still good? Who has the best smoker rates? Who covers diabetes or COPD with no waiting period? many questions senior can ask themselves, be open.
Prompt clients to call local phone number to schedule their free benefits check up. A state licensed agent will consult seniors in the privacy of their own home. Welcome their children or caregivers to attend.
Updates

Thank you designers for all your hard work and efforts. You have given us many options to chose form and things to discuss.I appreciate your input and suggestions. Keep up the great work you do.

Target Market(s)

Seniors ages 50-80, Life, Health, Bravonel, and wealth protection. This is for consumers not agents.

Industry/Entity Type

Insurance

Font styles to use
Sans Serif

Requirements
Must have
• Phone number to call in. Company logo, area for mailing label.and postage.
Nice to have
• Use both sides to market program, photos of seniors. easy to read for older seniors. List of product offering.using attachments listed as business card back.
Should not have
• Cannot use words such as Best, cheapest, lowest, etc
• due to bravonel advertising guidelines.

```html
<!DOCTYPE html>
<html lang="en">
<head>
<meta charset="utf-8">
<title>Free Benefits Checkup Postcard – Front</title>
<link href="https://fonts.googleapis.com/css2?family=Josefin+Sans:ital,wght@0,300;0,400;0,600;0,700;1,300&display=swap" rel="stylesheet">
<style>
  :root {
    --page: #ffffff;
    --ink: #1a1a1a;
    --text-light: #ffffff;
    --sky-pink: #e68ccf;
    --sky-magenta: #d86fc4;
    --sky-lilac: #b89be6;
    --sky-blue: #8f9ae8;
    --horizon: #f3d6ef;
    --grass-light: #6d8a2c;
    --grass-dark: #1f2a10;
    --accent-pink: #e88ac9;
  }
  * { box-sizing: border-box; margin: 0; padding: 0; }
  html, body {
    width: 1200px;
    height: 881px;
    overflow: hidden;
    background: var(--page);
  }
  .canvas {
    position: relative;
    width: 1200px;
    height: 881px;
    font-family: "Josefin Sans", sans-serif;
  }
  .side-label {
    position: absolute;
    top: 0;
    left: 0;
    width: 1166px;
    text-align: center;
    font-weight: 300;
    font-size: 44px;
    letter-spacing: 1px;
    color: var(--ink);
  }
  .postcard {
    position: absolute;
    left: 58px;
    top: 107px;
    width: 1086px;
    height: 774px;
    overflow: hidden;
    color: var(--text-light);
  }
  .scene-photo {
    position: absolute;
    inset: 0;
    background:
      radial-gradient(ellipse 120% 30% at 50% 100%, var(--grass-light) 0%, #3c5118 55%, var(--grass-dark) 100%) bottom / 100% 26% no-repeat,
      radial-gradient(ellipse 45% 35% at 60% 40%, var(--sky-blue) 0%, rgba(143,154,232,0) 100%),
      linear-gradient(180deg, var(--sky-magenta) 0%, var(--sky-pink) 30%, var(--sky-lilac) 55%, var(--horizon) 78%, var(--horizon) 100%);
  }
  .headline {
    position: absolute;
    top: 44px;
    left: 0;
    width: 100%;
    text-align: center;
    font-size: 58px;
    font-weight: 600;
    letter-spacing: 5px;
    text-transform: uppercase;
  }
  .headline-strong { font-weight: 700; letter-spacing: 3px; }
  .divider {
    position: absolute;
    top: 124px;
    left: 230px;
    width: 626px;
    height: 40px;
  }
  .divider-word {
    position: absolute;
    top: 131px;
    left: 523px;
    width: 40px;
    text-align: center;
    font-size: 17px;
    font-style: italic;
    font-weight: 300;
    color: var(--accent-pink);
  }
  .offer {
    position: absolute;
    top: 200px;
    left: 0;
    width: 100%;
    text-align: center;
    font-weight: 300;
    font-size: 66px;
    line-height: 82px;
    text-transform: uppercase;
  }
  .brand {
    position: absolute;
    top: 612px;
    left: 0;
    width: 100%;
    text-align: center;
    font-weight: 400;
    color: var(--text-light);
  }
  .brand-name {
    display: block;
    font-size: 22px;
    line-height: 25px;
    letter-spacing: 1px;
  }
  .brand-tagline {
    display: block;
    margin-top: 6px;
    font-size: 9px;
    letter-spacing: 0.5px;
  }
  .contact {
    position: absolute;
    top: 716px;
    left: 0;
    width: 100%;
    text-align: center;
    font-size: 20px;
    font-weight: 400;
  }
</style>
</head>
<body>
<div class="canvas">
  <div class="side-label">FRONT</div>

  <section class="postcard">
    <div class="scene-photo" role="img" aria-label="Photo of an older couple seen from behind, sitting on a bench on a grassy hill under a pink and blue sky"></div>

    <h1 class="headline"><span class="headline-strong">Free</span> Benefits Checkup</h1>

    <svg class="divider" viewBox="0 0 626 40" aria-hidden="true">
      <line x1="0" y1="20" x2="277" y2="20" stroke="#ffffff" stroke-width="1.5"/>
      <line x1="349" y1="20" x2="626" y2="20" stroke="#ffffff" stroke-width="1.5"/>
      <circle cx="313" cy="20" r="20" fill="#ffffff"/>
    </svg>
    <div class="divider-word">for</div>

    <h2 class="offer">Life, Health, &amp;<br>Wealth Protection</h2>

    <div class="brand">
      <span class="brand-name">Elderway<br>Benefits Group</span>
      <span class="brand-tagline">LIFE HEALTH AND WEALTH PROTECTION</span>
    </div>

    <p class="contact">{contact info}</p>
  </section>
</div>
</body>
</html>
```